Bref créative
Larchmere Restoring LLC
Bringing new life to old wood
Professional
Trent Holloway
owner
larchmererestore@mailvox.net
I need the following listed on the card.
Owners:
Trent Holloway 555 274 1906
Darby Fennimore 555 381 4527
Licensed and Insured
Free Estimates.
Hardwood floors and Cabinets. If it's made of wood we can renew it. Color changes or tints. Low odor, dust, and mess. A fraction of the cost vs refacing or replacement. Quick turnaround. Most jobs completed in 1-2 days.

```html
<!DOCTYPE html>
<html lang="en">
<head>
<meta charset="utf-8">
<title>Larchmere Restoring LLC – Business Card</title>
<link href="https://fonts.googleapis.com/css2?family=Open+Sans:wght@400;600;700&display=swap" rel="stylesheet">
<style>
  :root {
    --backdrop: #e9e2d6;
    --card-brown: #3b302a;
    --card-brown-dark: #2a221e;
    --stripe: rgba(0,0,0,0.16);
    --tan: #b89a72;
    --tan-light: #d2b88f;
    --ink-light: #f1ece6;
    --mark-grey: #b9b4ae;
  }
  * { margin: 0; padding: 0; box-sizing: border-box; }
  html, body {
    width: 1200px; height: 1047px; overflow: hidden;
    background: var(--backdrop);
    font-family: "Open Sans", Arial, sans-serif;
  }
  .canvas { position: relative; width: 1200px; height: 1047px; }
  .card {
    position: absolute; width: 760px; height: 440px;
    background:
      repeating-linear-gradient(135deg, transparent 0 70px, var(--stripe) 70px 110px, transparent 110px 190px),
      var(--card-brown);
    color: var(--ink-light);
    overflow: hidden;
    box-shadow: 0 10px 24px rgba(0,0,0,0.25);
  }
  .card--front { left: 120px; top: 60px; }
  .card--back { left: 320px; top: 547px; }

  .brand-square {
    position: absolute; width: 140px; height: 140px;
    background: var(--mark-grey);
  }
  .card--front .brand-square { left: 40px; top: 40px; }
  .brand-divider {
    position: absolute; left: 200px; top: 40px; width: 3px; height: 140px;
    background: var(--ink-light);
  }
  .brand-name {
    position: absolute; left: 220px; top: 48px;
    font-weight: 600; color: var(--ink-light);
    text-transform: uppercase; letter-spacing: 3px; line-height: 1.15;
  }
  .brand-name .line-one { display: block; font-size: 44px; }
  .brand-name .line-two { display: block; font-size: 27px; letter-spacing: 4px; }

  .contacts { position: absolute; left: 220px; top: 205px; }
  .contact { margin-bottom: 14px; }
  .contact__name { color: var(--tan-light); font-size: 21px; line-height: 1.2; }
  .contact__phone, .contact__email { font-size: 16px; line-height: 1.3; }
  .label { font-weight: 700; margin-right: 6px; }
  .contact__email { font-size: 17px; margin-top: 6px; }

  .tag-band {
    position: absolute; left: 0; right: 0; height: 44px;
    background: var(--card-brown-dark);
    border-top: 8px solid var(--tan);
    display: flex; align-items: center; justify-content: center;
    font-size: 22px; text-transform: uppercase; letter-spacing: 1px; color: var(--ink-light);
  }
  .card--front .tag-band { top: 352px; }
  .card--back .tag-band { top: 20px; border-top: none; border-bottom: 8px solid var(--tan); height: 52px; font-size: 25px; }

  .services {
    position: absolute; left: 40px; right: 40px; top: 100px;
    text-align: center; font-size: 18px; line-height: 1.4;
  }
  .card--back .brand-square { left: 310px; top: 260px; }
</style>
</head>
<body>
<main class="canvas">
  <section class="card card--front" aria-label="Card front">
    <div class="brand-square" aria-hidden="true"></div>
    <div class="brand-divider" aria-hidden="true"></div>
    <h1 class="brand-name">
      <span class="line-one">Larchmere</span>
      <span class="line-two">Restoring LLC</span>
    </h1>
    <div class="contacts">
      <div class="contact">
        <div class="contact__name">Trent Holloway</div>
        <div class="contact__phone"><span class="label">Cell:</span>555 274 1906</div>
      </div>
      <div class="contact">
        <div class="contact__name">Darby Fennimore</div>
        <div class="contact__phone"><span class="label">Cell:</span>555 381 4527</div>
      </div>
      <div class="contact__email"><span class="label">Email:</span>larchmererestore@mailvox.net</div>
    </div>
    <div class="tag-band">Licensed and insured, free estimates.</div>
  </section>

  <section class="card card--back" aria-label="Card back">
    <h2 class="tag-band">Bringing new life to old wood!</h2>
    <p class="services">
      Hardwood floors and Cabinets. If it's made of wood we can renew it.<br>
      Color changes or tints. Low odor, dust, and mess.<br>
      A fraction of the cost vs refacing or replacement.<br>
      Quick turnaround. Most jobs completed in 1-2 days.
    </p>
    <div class="brand-square" aria-hidden="true"></div>
  </section>
</main>
</body>
</html>
```